Theater Ad

A graphic for advertising in an indoor theater.
Target Market(s)
Parents of infants, toddlers, tweens and teens.
Industry/Entity Type
Pediatric Ophthalmology
Font styles to use
Sans Serif
Colors
EB3D1F
EC4F4E
F09395
F8D3D4
FCEDEE
Requirements
Must have
- Use the copy, color scheme, and photos shown in the attached older billboard advertisement, but in a new design for the theater.

Nice to have
- New design with both logos included

Should not have
- Just a single logo - must include both logos

```html
<!DOCTYPE html>
<html lang="en">
<head>
<meta charset="UTF-8">
<title>Theater Ad – Pediatric Eye Care</title>
<link href="https://fonts.googleapis.com/css2?family=Luckiest+Guy&family=Poppins:wght@400;500;600;700;800;900&display=swap" rel="stylesheet">
<style>
  :root{
    --stage:#c3c3c3;
    --paper:#ffffff;
    --brand-blue:#0e67c6;
    --band-blue:#1560c4;
    --band-deep:#0d4fa8;
    --kids-red:#e41e26;
    --navy:#10233f;
    --sun:#fff200;
    --badge:#f6b51c;
    --orange:#f26b1d;
    --white:#ffffff;
    --photo-warm:#d9b9a6;
    --photo-cool:#e7e3de;
  }
  *{box-sizing:border-box;margin:0;padding:0}
  html,body{width:1200px;height:888px;overflow:hidden;background:var(--stage)}
  .ad{
    position:absolute;left:40px;top:131px;width:1056px;height:590px;
    background:var(--paper);overflow:hidden;
    transform:scale(1.0606);transform-origin:0 0;
    font-family:'Poppins',sans-serif;
  }
  .brand{
    position:absolute;display:flex;align-items:center;gap:8px;
    font-family:'Poppins',sans-serif;font-weight:700;font-size:21px;line-height:1.1;
    color:var(--brand-blue);
  }
  .brand__dot{width:14px;height:14px;border-radius:50%;background:var(--brand-blue);flex:none}
  .brand--optical{left:62px;top:60px;width:190px}
  .brand--center{left:800px;top:60px;width:210px}
  .photo{position:absolute}
  .photo--left{left:10px;top:135px;width:320px;height:260px;border-radius:46% 46% 0 0;
    background:linear-gradient(180deg,var(--photo-warm),#b8322c 75%)}
  .photo--right{left:780px;top:130px;width:240px;height:270px;border-radius:46% 46% 0 0;
    background:linear-gradient(180deg,#6b4a3c,var(--photo-cool) 70%)}
  .photo--doctor{left:390px;top:325px;width:240px;height:265px;border-radius:48% 48% 0 0;
    background:linear-gradient(180deg,#b56a3a 0%,var(--photo-warm) 35%,#2a2a2a 65%)}
  .band{position:absolute;left:0;top:0;width:1056px;height:590px}
  .headline{
    position:absolute;left:250px;width:560px;text-align:center;
    font-family:'Luckiest Guy','Poppins',sans-serif;font-weight:900;
    text-transform:uppercase;line-height:1;white-space:nowrap;
  }
  .headline__lead{top:31px;font-size:62px;letter-spacing:-1px;color:var(--brand-blue)}
  .headline__kids{top:92px;font-size:170px;letter-spacing:-6px;color:var(--kids-red);text-shadow:-4px 4px 0 var(--navy)}
  .headline__tail{top:244px;font-size:60px;letter-spacing:-1px;color:var(--navy)}
  .badge{position:absolute;left:335px;top:345px;width:120px;height:110px}
  .badge__text{position:absolute;left:340px;top:377px;width:110px;text-align:center;
    font-family:'Luckiest Guy','Poppins',sans-serif;font-weight:800;text-transform:uppercase;
    font-size:18px;line-height:1.05;color:var(--navy);transform:rotate(-14deg)}
  .credentials{position:absolute;left:62px;top:410px;list-style:none;color:var(--white);font-size:17px;font-weight:500;line-height:24px}
  .credentials li{display:flex;align-items:center;gap:8px}
  .credentials svg{width:15px;height:15px;flex:none}
  .phone{position:absolute;left:62px;top:494px;display:flex;align-items:center;gap:6px;
    color:var(--white);font-weight:700;font-size:35px;line-height:1}
  .phone svg{width:30px;height:30px}
  .web{position:absolute;left:64px;top:535px;color:var(--white);font-size:17px;font-weight:500}
  .web b{color:var(--sun);font-weight:700}
  .nameplate{position:absolute;left:560px;top:422px;width:432px;height:72px;background:var(--kids-red);border-radius:0 36px 36px 0;padding:8px 0 0 122px}
  .nameplate__name{color:var(--white);font-weight:700;font-size:27px;line-height:1.1}
  .nameplate__title{color:var(--sun);font-weight:600;font-size:15px;letter-spacing:1px}
  .specialty{position:absolute;left:683px;top:506px;color:var(--white);font-size:20px;line-height:24px;font-weight:500}
</style>
</head>
<body>
<main class="ad">
  <div class="brand brand--optical"><span class="brand__dot"></span>Little Lens Optical</div>
  <div class="brand brand--center"><span class="brand__dot"></span>Bright Sprouts Eye Center</div>

  <div class="headline headline__lead">We Help</div>
  <div class="headline headline__kids">Kids</div>
  <div class="headline headline__tail">See Better!</div>

  <div class="photo photo--left" role="img" aria-label="Smiling young girl in large glasses and red plaid shirt pointing up"></div>
  <div class="photo photo--right" role="img" aria-label="Girl with dark wavy hair adjusting her glasses"></div>

  <svg class="band" viewBox="0 0 1056 590" aria-hidden="true">
    <defs>
      <linearGradient id="bandFill" x1="0" y1="0" x2="0" y2="1">
        <stop offset="0" stop-color="var(--band-blue)"/>
        <stop offset="1" stop-color="var(--band-deep)"/>
      </linearGradient>
    </defs>
    <path d="M560 378 C680 330 760 330 850 370 C930 400 990 370 1056 318 L1056 360 C990 400 920 420 840 395 C760 370 680 360 560 395 Z" fill="var(--sun)"/>
    <path d="M0 348 C120 330 230 340 330 352 L330 360 C230 350 120 345 0 360 Z" fill="var(--orange)"/>
    <path d="M0 356 C120 342 230 350 330 362 C400 330 470 320 540 340 C640 370 720 365 800 385 C880 405 960 395 1056 348 L1056 590 L0 590 Z" fill="url(#bandFill)"/>
  </svg>

  <div class="nameplate">
    <div class="nameplate__name">Marina Kestrel</div>
    <div class="nameplate__title">M.D, M.P.H.</div>
  </div>

  <div class="photo photo--doctor" role="img" aria-label="Smiling doctor with short auburn hair in polka-dot jacket"></div>

  <svg class="badge" viewBox="0 0 120 110" aria-hidden="true">
    <polygon points="60,2 78,16 102,12 106,36 120,55 106,74 102,98 78,94 60,108 42,94 18,98 14,74 0,55 14,36 18,12 42,16" fill="var(--badge)"/>
  </svg>
  <div class="badge__text">Se Habla<br>Espanol</div>

  <ul class="credentials">
    <li><svg viewBox="0 0 16 16"><circle cx="8" cy="8" r="8" fill="var(--sun)"/><path d="M4 8.3l2.6 2.5L12 5.4" stroke="var(--band-blue)" stroke-width="2" fill="none"/></svg>U.S Residency Trained</li>
    <li><svg viewBox="0 0 16 16"><circle cx="8" cy="8" r="8" fill="var(--sun)"/><path d="M4 8.3l2.6 2.5L12 5.4" stroke="var(--band-blue)" stroke-width="2" fill="none"/></svg>U.S Fellowship Trained</li>
    <li><svg viewBox="0 0 16 16"><circle cx="8" cy="8" r="8" fill="var(--sun)"/><path d="M4 8.3l2.6 2.5L12 5.4" stroke="var(--band-blue)" stroke-width="2" fill="none"/></svg>American Board Certified</li>
  </ul>

  <div class="phone">
    <svg viewBox="0 0 30 30" aria-hidden="true"><circle cx="15" cy="15" r="15" fill="var(--white)"/><path d="M10 8c1.5-1 2.5 0 3 1.5l.6 2c.2.8-.3 1.4-1 1.8 1 2 2.5 3.5 4.3 4.4.4-.7 1-1.2 1.8-1l2 .6c1.5.5 2.5 1.5 1.5 3-1 1.5-3 2-5 1.2C13 20 10 17 8.6 12.9 8 11 8.5 9 10 8z" fill="var(--navy)"/></svg>
    (555) 014 2837
  </div>
  <div class="web">www.<b>brightsproutseyes</b>.com</div>

  <div class="specialty">Pediatric Opthalmologist<br>Oftalmologia Pediatrica</div>
</main>
</body>
</html>
```